Stonebay Towing Business Card

Towing
Accident towing
Mechanical breakdown
Insurance, salvage and recovery
4wd off road towing
Light & Heavy towing
8347 2516
24 hour business 7 days

Logo can be whole size on front

Industry/Entity Type

Towing/ transport

Contact Information for Business Card

The above

```html
<!DOCTYPE html>
<html lang="en">
<head>
<meta charset="utf-8">
<title>Stonebay Towing Business Card</title>
<link rel="stylesheet" href="https://fonts.googleapis.com/css2?family=Montserrat:wght@400;600;800&display=swap">
<style>
  :root {
    --backdrop: #232325;
    --card: #232228;
    --card-edge: #d8202a;
    --red: #d8202a;
    --white: #ffffff;
    --tone-mark: #3b3b40;
    --tone-mark-small: #38383d;
  }
  html, body {
    margin: 0;
    padding: 0;
    width: 1200px;
    height: 780px;
    overflow: hidden;
    background: var(--backdrop);
    font-family: "Montserrat", Arial, sans-serif;
  }
  .stage {
    position: relative;
    width: 1200px;
    height: 780px;
  }
  .card {
    position: absolute;
    width: 540px;
    height: 310px;
    background: var(--card);
    border-radius: 18px;
    box-shadow: 0 5px 0 var(--card-edge);
    overflow: hidden;
  }
  .card-front { left: 60px; top: 70px; }
  .card-back { left: 600px; top: 390px; }

  .front-name {
    position: absolute;
    inset: 0;
    display: flex;
    align-items: center;
    justify-content: center;
    text-align: center;
    font-weight: 800;
    font-size: 54px;
    line-height: 1.05;
    color: var(--tone-mark);
  }

  .back-name-small {
    position: absolute;
    left: 34px;
    top: 30px;
    font-weight: 800;
    font-size: 22px;
    line-height: 1.05;
    color: var(--tone-mark-small);
  }

  .phone {
    position: absolute;
    right: 30px;
    top: 30px;
    display: flex;
    align-items: center;
    gap: 10px;
    color: var(--white);
    font-size: 16px;
    font-weight: 400;
    letter-spacing: 0.5px;
  }
  .phone svg { width: 18px; height: 18px; }

  .services {
    position: absolute;
    left: 34px;
    bottom: 28px;
    margin: 0;
    padding: 0;
    list-style: none;
    color: var(--white);
    font-size: 13.5px;
    line-height: 21px;
  }
  .services li {
    display: flex;
    align-items: center;
    gap: 12px;
  }
  .services li::before {
    content: "";
    width: 8px;
    height: 8px;
    border-radius: 50%;
    background: var(--red);
    flex: none;
  }

  .back-name-large {
    position: absolute;
    right: 28px;
    bottom: 40px;
    text-align: right;
    font-weight: 800;
    font-size: 40px;
    line-height: 1.05;
    color: var(--red);
  }
</style>
</head>
<body>
<main class="stage">

  <section class="card card-front" aria-label="Card front">
    <div class="front-name">Stonebay<br>Towing</div>
  </section>

  <section class="card card-back" aria-label="Card back">
    <div class="back-name-small">Stonebay<br>Towing</div>

    <div class="phone">
      <span class="phone-number">8347 2516</span>
      <svg viewBox="0 0 24 24" aria-hidden="true">
        <path fill="var(--red)" d="M3 9c0-2 4-4 9-4s9 2 9 4v2h-5V9c-1-.6-2.4-1-4-1s-3 .4-4 1v2H3z"/>
        <path fill="var(--red)" d="M6 13l2-3h8l2 3v6H6z"/>
        <circle cx="12" cy="15.5" r="2" fill="var(--card)"/>
      </svg>
    </div>

    <ul class="services">
      <li>Towing</li>
      <li>Accident towing</li>
      <li>Mechanical breakdown</li>
      <li>Insurance, salvage and recovery</li>
      <li>4wd off road towing</li>
      <li>Light &amp; Heavy towing</li>
      <li>24/7 business</li>
    </ul>

    <div class="back-name-large">Stonebay<br>Towing</div>
  </section>

</main>
</body>
</html>
```